Doctors Office Web Design

Name of the business is Lian-Hua Qiu M.D.
We need a web design that is attractive for women that want to see Dr. Lian-Hua Qiu for Obstetrician Gynecology and Pregnancy care. Dr. Qiu earned her degree from Harbor Crest Medical College of obstetrician gynecology. We want to attract women of child bearing ages to come to our offices for health, education, and pregnancies.

Please visit http://www.drqiucare-example.com/ to help you get a feel for who we are. We will be adding some pictures and logo in the next few days.

We are looking for to have pages for and tabs including
About Us- History, Our Staff, Dr. Qiu
Patient Information- Appointments, E-Prescriptions, Payments Accepted, Insurance
Health- General, Sexual, Mental, Affiliates
Pregnancy- Minimally invasive surgery(our specialty), 4-D Ultra Sound, Hospital Affiliations
Media- News,Pictures, Videos
Locations- Palmvale Office, Marlow Office

The colors we would like to use are pastel colors, magenta, and plum

Target Market(s)

Women of all ages with an emphasis on 25-65 year olds

Industry/Entity Type

Business

Requirements
Must have
• Needs to include a location for a our videos and pictures that I will submit shortly. We also want a map to our location or atleast a place for one.
Nice to have
• A place for a google map of our office locations.

```html
<!DOCTYPE html>
<html lang="en">
<head>
<meta charset="utf-8">
<title>Lian-Hua Qiu M.D</title>
<link href="https://fonts.googleapis.com/css2?family=Arimo:ital,wght@0,400;0,700;1,400&display=swap" rel="stylesheet">
<style>
  :root {
    --plum: #3c1852;
    --plum-text: #4a1f70;
    --header-bg: #f3f2ee;
    --beige: #c5baa6;
    --white: #ffffff;
    --ink: #1e1e1e;
    --nav-ink: #333333;
    --sheet-light: #fbfbfa;
    --sheet-mid: #e9e8e6;
    --sheet-shade: #d9d8d6;
  }
  * { margin: 0; padding: 0; box-sizing: border-box; }
  html, body { width: 1200px; height: 900px; overflow: hidden; }
  body {
    font-family: "Arimo", Arial, sans-serif;
    color: var(--ink);
    background: var(--plum);
    position: relative;
  }
  .header {
    position: absolute; left: 0; top: 0; width: 1200px; height: 305px;
    background: var(--header-bg);
    overflow: hidden;
  }
  .hero-photo {
    position: absolute; left: 480px; top: 0; width: 720px; height: 305px;
    background:
      linear-gradient(90deg, var(--header-bg) 0%, rgba(243,242,238,0) 22%),
      radial-gradient(ellipse 180px 150px at 300px 150px, var(--sheet-light) 0%, rgba(251,251,250,0) 100%),
      radial-gradient(ellipse 160px 120px at 560px 90px, #f7f7f6 0%, rgba(247,247,246,0) 100%),
      radial-gradient(ellipse 260px 90px at 420px 300px, var(--sheet-shade) 0%, rgba(217,216,214,0) 100%),
      linear-gradient(160deg, var(--sheet-mid) 0%, #f1f1ef 40%, #e4e3e1 70%, #efeeec 100%);
  }
  .brand { position: absolute; left: 60px; top: 38px; width: 210px; text-align: center; }
  .brand-mark {
    width: 188px; height: 188px; border-radius: 50%;
    background: var(--beige); margin: 0 auto;
    display: flex; align-items: center; justify-content: center;
    color: var(--white); font-size: 24px; line-height: 30px; text-align: center;
  }
  .brand-name {
    margin-top: 16px; font-size: 19px; color: var(--plum-text);
  }
  .nav {
    position: absolute; left: 0; top: 305px; width: 1200px; height: 44px;
    background: linear-gradient(#ffffff, #f1efec);
    border-top: 1px solid #e8e6e2;
  }
  .nav-item {
    position: absolute; top: 13px; font-size: 16.5px; color: var(--nav-ink);
    transform: translateX(-50%); white-space: nowrap;
  }
  .nav-item.is-active { font-weight: 700; }
  .dropdown {
    position: absolute; left: 278px; top: 349px; width: 184px; height: 163px;
    background: linear-gradient(#ebe8e3, #f6f5f3);
    box-shadow: 0 2px 4px rgba(0,0,0,.15);
    z-index: 3;
  }
  .dropdown-item {
    height: 36px; line-height: 36px; padding-left: 33px; font-size: 13px; color: var(--nav-ink);
  }
  .dropdown-item:first-child { margin-top: 14px; }
  .dropdown-item.is-current { background: #e4e1dc; color: var(--plum-text); }
  .panel { position: absolute; background: var(--white); }
  .news { left: 12px; top: 367px; width: 860px; height: 313px; }
  .feature { left: 12px; top: 689px; width: 860px; height: 220px; }
  .thumb {
    position: absolute; width: 137px;
    background: linear-gradient(160deg, #cfd5d8 0%, #e9e4dd 45%, #9aa77e 80%, #6d7a4d 100%);
  }
  .story { position: absolute; width: 210px; }
  .story h3, .feature h3 { font-size: 13.5px; font-weight: 700; margin-bottom: 10px; }
  .story p, .feature p { font-size: 12.5px; line-height: 17px; }
  .read-more { display: block; margin-top: 4px; font-size: 13px; font-style: italic; color: var(--plum-text); }
  .guest-tab {
    position: absolute; left: 583px; top: 0; width: 277px; height: 27px;
    background: var(--beige); color: var(--white); font-size: 12px; line-height: 27px; padding-left: 13px;
  }
  .guest-tab span { color: var(--plum-text); }
  .feature .body { position: absolute; left: 166px; top: 28px; width: 662px; }
  .feature p { font-size: 12.3px; line-height: 17.3px; }
  .doctor-photo {
    position: absolute; left: 884px; top: 367px; width: 302px; height: 310px;
    background: linear-gradient(180deg, #dfe3e3 0%, #eef0ef 40%, #f1a85a 75%, #ee9a45 100%);
  }
  .quote {
    position: absolute; left: 884px; top: 677px; width: 302px; height: 127px;
    background: var(--beige); color: var(--white); padding: 21px 30px;
  }
  .quote p { font-style: italic; font-size: 18.5px; line-height: 25px; }
  .quote .author { font-style: normal; font-size: 17px; margin-top: 10px; }
  .contact {
    position: absolute; left: 884px; top: 816px; width: 302px; height: 84px;
    background: var(--white); padding: 25px 30px; font-size: 15.5px; font-weight: 700; line-height: 20px;
  }
</style>
</head>
<body>
  <header class="header">
    <div class="hero-photo" role="img" aria-label="Photo of a smiling baby lying on white bed sheets"></div>
    <div class="brand">
      <div class="brand-mark">Lian-Hua<br>Qiu M.D</div>
      <div class="brand-name">Lian-Hua Qiu M.D</div>
    </div>
  </header>

  <nav class="nav">
    <span class="nav-item is-active" style="left:100px">Home</span>
    <span class="nav-item" style="left:216px">About us</span>
    <span class="nav-item" style="left:374px">Patient Information</span>
    <span class="nav-item" style="left:519px">Health</span>
    <span class="nav-item" style="left:634px">Pregnancy</span>
    <span class="nav-item" style="left:762px">Affiliations</span>
    <span class="nav-item" style="left:882px">Media</span>
    <span class="nav-item" style="left:1008px">Locations</span>
  </nav>

  <div class="dropdown">
    <div class="dropdown-item">Appointments</div>
    <div class="dropdown-item">E-Prescriptions</div>
    <div class="dropdown-item">Payments Accepted</div>
    <div class="dropdown-item is-current">Insurance</div>
  </div>

  <section class="panel news">
    <div class="thumb" style="left:14px;top:16px;height:127px" role="img" aria-label="Photo of a pregnant woman outdoors"></div>
    <div class="story" style="left:166px;top:16px">
      <h3>Pregnancy</h3>
      <p>Lorem ipsum dolor sit amet, consect-etur adipiscing elit. Curabitur eu est nisi. Morbi et est nec risus adipiscing scelerisque at ut velit.</p>
      <span class="read-more">Read more</span>
    </div>
    <div class="thumb" style="left:431px;top:16px;height:127px" role="img" aria-label="Photo of a pregnant woman outdoors"></div>
    <div class="story" style="left:583px;top:16px">
      <h3>New technology update</h3>
      <p>Lorem ipsum dolor sit amet, consect-etur adipiscing elit. Curabitur eu est nisi. Morbi et est nec risus adipiscing scelerisque at ut velit.</p>
      <span class="read-more">Read more</span>
    </div>
    <div class="thumb" style="left:14px;top:171px;height:127px" role="img" aria-label="Photo of a pregnant woman outdoors"></div>
    <div class="story" style="left:166px;top:171px">
      <h3>Getting an ultrasound</h3>
      <p>Lorem ipsum dolor sit amet, consect-etur adipiscing elit. Curabitur eu est nisi. Morbi et est nec risus adipiscing scelerisque at ut velit.</p>
      <span class="read-more">Read more</span>
    </div>
    <div class="thumb" style="left:431px;top:171px;height:127px" role="img" aria-label="Photo of a pregnant woman outdoors"></div>
    <div class="story" style="left:583px;top:171px">
      <h3>Opening of new location</h3>
      <p>Lorem ipsum dolor sit amet, consect-etur adipiscing elit. Curabitur eu est nisi. Morbi et est nec risus adipiscing scelerisque at ut velit.</p>
      <span class="read-more">Read more</span>
    </div>
  </section>

  <section class="panel feature">
    <div class="guest-tab">GUEST COLUMN BY <span>NORA ELLISON</span></div>
    <div class="thumb" style="left:14px;top:29px;height:161px" role="img" aria-label="Photo of a pregnant woman outdoors"></div>
    <div class="body">
      <h3>The first weeks</h3>
      <p>Lorem ipsum dolor sit amet, consectetur adipiscing elit. Maecenas id sapien lacus, a volutpat justo. Etiam odio quam, varius sed lobortis sed, commodo vel risus. In hac habitasse platea dictumst. Vestibulum in sapien a justo malesuada posuere. Fusce et dolor sed lacus facilisis molestie. Aenean venenatis, orci porta consectetur mattis, libero risus sodales magna, non gravida leo orci sit amet tellus. Integer luctus ante a nunc vulputate accumsan. Aenean metus massa, facilisis quis commodo et, porta nec lectus. Cum sociis natoque penatibus et magnis dis parturient montes, nascetur ridiculus mus. Suspendisse at turpis sed nibh suscipit eleifend. Sed elementum tristique mi, in vestibulum nunc sollicitudin vel. Ut sollicitudin sodales magna, eu tempus eros vehicula quis. Duis et tempus turpis.</p>
      <span class="read-more">Read more</span>
    </div>
  </section>

  <div class="doctor-photo" role="img" aria-label="Photo of a smiling doctor in orange scrubs with a stethoscope"></div>
  <aside class="quote">
    <p>“Lorem ipsum dolor sit amet, consectetur adipiscing elit.“</p>
    <p class="author">Lian-Hua Qiu M.D</p>
  </aside>
  <aside class="contact">
    Do you wish to meet dr. Qiu?<br>Call (555) 014-2290
  </aside>
</body>
</html>
```